Varlen Structural Approval Standards Private Assessors

Professional Construction Consultancy Company Business Card - must keep logo colours see images below - examples have been added from my last competition - please see them as examples only!

Target Market(s)

Home Builders

Industry/Entity Type

Construction

Contact Information for Business Card

See "must haves"

Font styles to use
Sans Serif

Colors
ffffff
add136
000000

Requirements
Must have
• Daniel Moravi
• Director
• Phone: 0431 587 219
• Address: 7 Tarrunga Rd,
• Hallworth Vale, SA, 5091
• Email: varlenassessors@mailbox-example.com
• Website: www.varlenassessors-example.com.au
• Facebook: Varlen Structural Approval Standards
Nice to have
• Side 1: full logo
• Side 2: company details
Should not have
• hard to read
• must be clear and professional

```html
<!DOCTYPE html>
<html lang="en">
<head>
<meta charset="utf-8">
<title>Varlen Structural Approval Standards – Business Card</title>
<link rel="stylesheet" href="https://fonts.googleapis.com/css2?family=Source+Sans+3:wght@400;600;700&display=swap">
<style>
  :root {
    --backdrop: #a4a4a4;
    --card-white: #f3f3f3;
    --brand-green: #80b135;
    --ink: #1c1c1c;
    --text-grey: #4d4d4d;
    --divider: #c4c4c4;
    --soft-white: #eef3e4;
  }
  * { box-sizing: border-box; margin: 0; padding: 0; }
  html, body {
    width: 1105px;
    height: 1200px;
    overflow: hidden;
  }
  body {
    background: var(--backdrop);
    font-family: "Source Sans 3", Arial, sans-serif;
    position: relative;
  }
  .card {
    position: absolute;
    left: 182px;
    width: 746px;
    height: 427px;
    overflow: hidden;
  }
  .card--front { top: 119px; background: var(--card-white); }
  .card--back { top: 636px; background: var(--brand-green); }

  .brand {
    display: flex;
    align-items: center;
    gap: 14px;
    font-weight: 700;
    line-height: 1.12;
  }
  .brand__square {
    flex: none;
    width: 46px;
    height: 46px;
  }
  .brand__name { font-size: 22px; }

  .card--front .brand {
    position: absolute;
    left: 56px;
    top: 150px;
    width: 300px;
    color: var(--ink);
  }
  .card--front .brand__square { background: var(--brand-green); }

  .front__divider {
    position: absolute;
    left: 384px;
    top: 85px;
    width: 1px;
    height: 235px;
    background: var(--divider);
  }
  .contact {
    position: absolute;
    left: 406px;
    top: 70px;
    width: 330px;
    color: var(--text-grey);
    font-size: 18px;
    line-height: 1.3;
  }
  .contact__name {
    color: var(--brand-green);
    font-size: 27px;
    font-weight: 600;
    line-height: 1.2;
  }
  .contact__role {
    color: var(--ink);
    font-size: 19px;
    margin-bottom: 12px;
  }
  .contact__address { margin-bottom: 8px; }
  .contact__list { list-style: none; }
  .contact__item {
    display: flex;
    align-items: center;
    gap: 9px;
    height: 30px;
    white-space: nowrap;
  }
  .contact__icon {
    width: 17px;
    height: 17px;
    flex: none;
    fill: var(--brand-green);
  }
  .contact__square {
    width: 15px;
    height: 15px;
    flex: none;
    background: var(--brand-green);
    margin: 0 1px;
  }
  .front__rule {
    position: absolute;
    left: 0;
    bottom: 35px;
    width: 100%;
    height: 3px;
    background: var(--ink);
  }
  .front__band {
    position: absolute;
    left: 0;
    bottom: 0;
    width: 100%;
    height: 33px;
    background: var(--brand-green);
  }

  .card--back .brand {
    position: absolute;
    left: 50%;
    top: 150px;
    transform: translateX(-50%);
    width: 380px;
    color: #ffffff;
  }
  .card--back .brand__square { background: #ffffff; }
  .card--back .brand__name { font-size: 26px; }
  .back__web {
    position: absolute;
    left: 0;
    top: 356px;
    width: 100%;
    text-align: center;
    color: var(--soft-white);
    font-size: 19px;
    letter-spacing: 1.6px;
  }
</style>
</head>
<body>
  <section class="card card--front" aria-label="Card front">
    <div class="brand">
      <span class="brand__square"></span>
      <span class="brand__name">Varlen Structural Approval Standards Private Assessors</span>
    </div>
    <div class="front__divider"></div>
    <div class="contact">
      <p class="contact__name">Daniel Moravi</p>
      <p class="contact__role">Director</p>
      <p class="contact__address">7 Tarrunga Rd,<br>Hallworth Vale, SA, 5091</p>
      <ul class="contact__list">
        <li class="contact__item">
          <svg class="contact__icon" viewBox="0 0 24 24" aria-hidden="true"><path d="M6.6 10.8c1.4 2.8 3.8 5.1 6.6 6.6l2.2-2.2c.3-.3.7-.4 1-.2 1.1.4 2.3.6 3.6.6.6 0 1 .4 1 1V20c0 .6-.4 1-1 1C10.6 21 3 13.4 3 4c0-.6.4-1 1-1h3.5c.6 0 1 .4 1 1 0 1.3.2 2.5.6 3.6.1.3 0 .7-.2 1z"/></svg>
          <span>0431 587 219</span>
        </li>
        <li class="contact__item">
          <svg class="contact__icon" viewBox="0 0 24 24" aria-hidden="true"><path d="M2 5h20v14H2z M3.5 6.5 12 13l8.5-6.5" fill="none" stroke="#80b135" stroke-width="2"/><path d="M2 5h20v14H2z" opacity=".35"/></svg>
          <span>varlenassessors@mailbox-example.com</span>
        </li>
        <li class="contact__item">
          <svg class="contact__icon" viewBox="0 0 24 24" aria-hidden="true"><circle cx="12" cy="12" r="9.5" fill="none" stroke="#80b135" stroke-width="2"/><path d="M2.5 12h19M12 2.5c3 3 3 16 0 19M12 2.5c-3 3-3 16 0 19" fill="none" stroke="#80b135" stroke-width="1.6"/></svg>
          <span>www.varlenassessors-example.com.au</span>
        </li>
        <li class="contact__item">
          <span class="contact__square"></span>
          <span>Varlen Structural Approval Standards</span>
        </li>
      </ul>
    </div>
    <div class="front__rule"></div>
    <div class="front__band"></div>
  </section>

  <section class="card card--back" aria-label="Card back">
    <div class="brand">
      <span class="brand__square"></span>
      <span class="brand__name">Varlen Structural Approval Standards Private Assessors</span>
    </div>
    <p class="back__web">www.varlenassessors-example.com.au</p>
  </section>
</body>
</html>
```